BPH Business Card 2018

Brellmore Chiropractic. We have two locations that we want to advertise on the same card. Calderwick OrthoAxis campus address: 3815 Pemberly Dr., Suite 240, Flowood, MS 39587. Madison address: 426 Larkmoor Dr., Building D., Madison, MS 39674. website: www.drbrellmore.example. o:(601)555-0148 f:(601)555-0173

Target Market(s)

Health care decision makers: primary care doctors and mothers

Contact Information for Business Card

I have no idea; up for any suggestions and I'd do much better picking from examples versus describing what I'm looking for. We are in a very high end location and would like the cards to look really sharp.

Requirements
Must have
• My name, Tobias R Venmark, D.C.

```html
<!DOCTYPE html>
<html lang="en">
<head>
<meta charset="utf-8">
<title>Brellmore Chiropractic — Business Card</title>
<link rel="stylesheet" href="https://fonts.googleapis.com/css2?family=Cinzel:wght@400;600&family=Lato:wght@400;700&display=swap">
<style>
  :root {
    --canvas: #eceae7;
    --card-dark: #000000;
    --card-light: #ffffff;
    --ink-light: #ffffff;
    --ink-dark: #111111;
    --figure-hi: #f6f6f6;
    --figure-mid: #d9d9d9;
    --figure-lo: #a8a8a8;
  }
  * { margin: 0; padding: 0; box-sizing: border-box; }
  html, body { width: 1200px; height: 900px; overflow: hidden; }
  body { background: var(--canvas); position: relative; font-family: "Lato", sans-serif; }

  .card { position: absolute; width: 612px; height: 364px; box-shadow: 0 6px 18px rgba(0,0,0,.18); overflow: hidden; }
  .card--front { left: 174px; top: 52px; background: var(--card-dark); color: var(--ink-light); }
  .card--back  { left: 541px; top: 476px; background: var(--card-light); color: var(--ink-dark); }

  .brand { position: absolute; font-family: "Cinzel", serif; font-weight: 400; line-height: 1; white-space: nowrap; }
  .brand__line { display: block; }
  .card--front .brand { left: 123px; top: 56px; }
  .card--front .brand__line--name { font-size: 36px; letter-spacing: .5px; }
  .card--front .brand__line--trade { font-size: 24px; margin-top: 1px; }

  .card--back .brand { left: 200px; top: 96px; color: var(--ink-dark); }
  .card--back .brand__line--name { font-size: 50px; letter-spacing: .5px; }
  .card--back .brand__line--trade { font-size: 35px; margin-top: 2px; }

  .practitioner { position: absolute; left: 51px; top: 189px; font-family: "Cinzel", serif; font-weight: 600; font-size: 20px; letter-spacing: 1px; white-space: nowrap; }

  .contact { position: absolute; left: 51px; top: 270px; list-style: none; font-size: 15.5px; line-height: 22px; }

  .feature-figure { position: absolute; left: 398px; top: 108px; width: 260px; height: 420px;
    background: radial-gradient(closest-side, var(--figure-hi) 0%, var(--figure-mid) 60%, var(--figure-lo) 92%, transparent 100%); }

  .locations { position: absolute; left: 0; right: 0; top: 228px; text-align: center; font-size: 15.5px; line-height: 21px; }
  .location { margin-bottom: 12px; }
  .location__title { font-weight: 700; text-transform: uppercase; }
</style>
</head>
<body>
  <section class="card card--front">
    <div class="brand">
      <span class="brand__line brand__line--name">BRELLMORE</span>
      <span class="brand__line brand__line--trade">Chiropractic</span>
    </div>
    <p class="practitioner">TOBIAS R VENMARK, D.C.</p>
    <ul class="contact">
      <li>P: (601)555-0148</li>
      <li>F: (601)555-0173</li>
      <li>www.drbrellmore.example</li>
    </ul>
    <div class="feature-figure" role="img" aria-label="Decorative illustration of an athletic figure"></div>
  </section>

  <section class="card card--back">
    <div class="brand">
      <span class="brand__line brand__line--name">BRELLMORE</span>
      <span class="brand__line brand__line--trade">Chiropractic</span>
    </div>
    <div class="locations">
      <div class="location">
        <p class="location__title">Calderwick OrthoAxis Campus</p>
        <p class="location__address">3815 Pemberly Dr., Suite 240 Flowood, MS 39587.</p>
      </div>
      <div class="location">
        <p class="location__title">Madison</p>
        <p class="location__address">426 Larkmoor Dr., Building D., Madison, MS 39674.</p>
      </div>
    </div>
  </section>
</body>
</html>
```